Website - User Access Door - Images

4 separate images that fit together to form a door that I will animate to open up when a user accesses my website. 1. Left Door 2. Right Door. 3. Lock (open) 4. Lock (closed). High resolution as it must look good on huge monitors.

Attached is a picture very close to what I'm after. I guess the main thing to keep in mind is that it needs to look strong. The attached graphic is quite close to what I'm after, but I need a unique design, not a copy of this one.

Reason: I was promised more than 3 submissions by PixelNook. I guess they need more time...

Here are some images for inspiration. Think Soviet iron nuclear bunker door. Heavy, Strong (but latest technology incorporated)

http://img4.lorvipedia.net/__cb20090716105544/vortra/images/1/1d/KTRF_bunker_door.jpg

http://www.tobiasrenderworks.com/QRT_Bunker3_TobiasKrell.jpg

Nice texture ideas:
http://www.surfacevault.com/data/media/8/steel_door_texture.jpg

Think games:
http://www.stagerundown.com/ironveil/zone7b/24.jpg

http://brightmosaic.com/wp-content/uploads/2013/09/Metal-Door-Wall-Graphic-Decals.jpg

```html
<!DOCTYPE html>
<html lang="en">
<head>
<meta charset="utf-8">
<title>User Access Door</title>
<link rel="stylesheet" href="https://fonts.googleapis.com/css2?family=Roboto:wght@400&display=swap">
<style>
  :root {
    --void: #000000;
    --glow: #ffffff;
    --edge-dark: #161616;
    --panel-dark: #111111;
    --panel-mid: #5e5e5e;
    --steel-light: #e4e4e4;
    --steel-mid: #9a9a9a;
    --steel-dark: #444444;
    --steel-deep: #1a1a1a;
    --lock-shadow: #050505;
    --lamp-bright: #d8ffc8;
    --lamp: #2ee81a;
    --lamp-deep: #0a8a05;
  }
  html, body {
    margin: 0;
    padding: 0;
    width: 1200px;
    height: 900px;
    overflow: hidden;
    background: var(--void);
    font-family: "Roboto", sans-serif;
  }
  .door-scene { display: block; width: 1200px; height: 900px; }
  .stop-void { stop-color: var(--void); }
  .stop-glow { stop-color: var(--glow); }
  .stop-edge-dark { stop-color: var(--edge-dark); }
  .stop-panel-dark { stop-color: var(--panel-dark); }
  .stop-panel-mid { stop-color: var(--panel-mid); }
  .stop-steel-light { stop-color: var(--steel-light); }
  .stop-steel-mid { stop-color: var(--steel-mid); }
  .stop-steel-dark { stop-color: var(--steel-dark); }
  .stop-steel-deep { stop-color: var(--steel-deep); }
  .stop-lock-shadow { stop-color: var(--lock-shadow); }
  .stop-lamp-bright { stop-color: var(--lamp-bright); }
  .stop-lamp { stop-color: var(--lamp); }
  .stop-lamp-deep { stop-color: var(--lamp-deep); }
</style>
</head>
<body>
<svg class="door-scene" viewBox="0 0 1200 900" xmlns="http://www.w3.org/2000/svg" role="img" aria-label="Heavy steel left and right door leaves closed around a round central lock with two green lights">
  <defs>
    <linearGradient id="wall-glow" x1="0" y1="0" x2="0" y2="1">
      <stop offset="0" class="stop-void"/>
      <stop offset="0.12" class="stop-void"/>
      <stop offset="0.3" class="stop-steel-dark"/>
      <stop offset="0.5" class="stop-glow"/>
      <stop offset="0.7" class="stop-steel-dark"/>
      <stop offset="0.88" class="stop-void"/>
      <stop offset="1" class="stop-void"/>
    </linearGradient>
    <linearGradient id="panel-face" x1="0" y1="0" x2="0" y2="1">
      <stop offset="0" class="stop-panel-dark"/>
      <stop offset="0.5" class="stop-panel-mid"/>
      <stop offset="1" class="stop-panel-dark"/>
    </linearGradient>
    <linearGradient id="frame-steel-v" x1="0" y1="0" x2="0" y2="1">
      <stop offset="0" class="stop-steel-dark"/>
      <stop offset="0.5" class="stop-steel-light"/>
      <stop offset="1" class="stop-steel-dark"/>
    </linearGradient>
    <linearGradient id="frame-steel-h" x1="0" y1="0" x2="0" y2="1">
      <stop offset="0" class="stop-steel-light"/>
      <stop offset="1" class="stop-steel-dark"/>
    </linearGradient>
    <linearGradient id="ring-outer" x1="0.15" y1="0.85" x2="0.85" y2="0.15">
      <stop offset="0" class="stop-steel-dark"/>
      <stop offset="0.25" class="stop-glow"/>
      <stop offset="0.55" class="stop-steel-mid"/>
      <stop offset="0.8" class="stop-steel-deep"/>
      <stop offset="1" class="stop-steel-mid"/>
    </linearGradient>
    <linearGradient id="ring-inner" x1="0" y1="0" x2="0" y2="1">
      <stop offset="0" class="stop-lock-shadow"/>
      <stop offset="0.5" class="stop-steel-dark"/>
      <stop offset="1" class="stop-glow"/>
    </linearGradient>
    <linearGradient id="ring-lip" x1="0" y1="0" x2="0" y2="1">
      <stop offset="0" class="stop-steel-light"/>
      <stop offset="0.5" class="stop-steel-mid"/>
      <stop offset="1" class="stop-steel-deep"/>
    </linearGradient>
    <linearGradient id="lock-face" x1="0" y1="0" x2="0" y2="1">
      <stop offset="0" class="stop-lock-shadow"/>
      <stop offset="0.25" class="stop-steel-dark"/>
      <stop offset="0.5" class="stop-steel-light"/>
      <stop offset="0.75" class="stop-steel-mid"/>
      <stop offset="1" class="stop-lock-shadow"/>
    </linearGradient>
    <linearGradient id="key-slot" x1="0" y1="0" x2="1" y2="0">
      <stop offset="0" class="stop-steel-deep"/>
      <stop offset="0.55" class="stop-steel-mid"/>
      <stop offset="1" class="stop-steel-dark"/>
    </linearGradient>
    <radialGradient id="lamp-glow" cx="0.42" cy="0.35" r="0.7">
      <stop offset="0" class="stop-lamp-bright"/>
      <stop offset="0.4" class="stop-lamp"/>
      <stop offset="1" class="stop-lamp-deep"/>
    </radialGradient>
    <radialGradient id="lamp-bezel" cx="0.5" cy="0.3" r="0.7">
      <stop offset="0" class="stop-steel-light"/>
      <stop offset="1" class="stop-lock-shadow"/>
    </radialGradient>
  </defs>

  <rect class="wall" x="0" y="0" width="1200" height="900" fill="url(#wall-glow)"/>
  <rect class="wall-recess" x="56" y="41" width="1090" height="816" fill="var(--void)"/>

  <g class="door-left">
    <rect class="door-frame" x="60" y="45" width="539" height="808" fill="url(#frame-steel-v)"/>
    <rect class="door-frame-top" x="60" y="45" width="539" height="15" fill="url(#frame-steel-h)"/>
    <rect class="door-frame-bottom" x="60" y="840" width="539" height="13" fill="var(--steel-dark)"/>
    <rect class="door-frame-edge" x="60.5" y="45.5" width="538" height="807" fill="none" stroke="var(--steel-deep)" stroke-width="1"/>
    <rect class="door-panel-rim" x="70" y="58" width="518" height="784" fill="var(--steel-deep)"/>
    <rect class="door-panel" x="72" y="60" width="514" height="780" fill="url(#panel-face)"/>
  </g>

  <g class="door-right">
    <rect class="door-frame" x="603" y="45" width="539" height="808" fill="url(#frame-steel-v)"/>
    <rect class="door-frame-top" x="603" y="45" width="539" height="15" fill="url(#frame-steel-h)"/>
    <rect class="door-frame-bottom" x="603" y="840" width="539" height="13" fill="var(--steel-dark)"/>
    <rect class="door-frame-edge" x="603.5" y="45.5" width="538" height="807" fill="none" stroke="var(--steel-deep)" stroke-width="1"/>
    <rect class="door-panel-rim" x="615" y="58" width="518" height="784" fill="var(--steel-deep)"/>
    <rect class="door-panel" x="617" y="60" width="514" height="780" fill="url(#panel-face)"/>
  </g>

  <rect class="door-seam" x="599" y="45" width="4" height="808" fill="var(--lock-shadow)"/>

  <g class="door-lock">
    <circle class="lock-shadow" cx="603" cy="443" r="121" fill="var(--lock-shadow)" opacity="0.55"/>
    <circle class="lock-bezel" cx="600" cy="440" r="120" fill="url(#ring-outer)" stroke="var(--steel-deep)" stroke-width="2"/>
    <circle class="lock-groove" cx="600" cy="440" r="95" fill="url(#ring-inner)"/>
    <circle class="lock-lip" cx="600" cy="440" r="90" fill="url(#ring-lip)"/>
    <circle class="lock-face" cx="600" cy="440" r="84" fill="url(#lock-face)"/>
    <rect class="lock-slot-rim" x="586" y="398" width="30" height="87" fill="var(--lock-shadow)"/>
    <rect class="lock-slot" x="592" y="404" width="18" height="75" fill="url(#key-slot)"/>
    <polygon class="lock-slot-bevel" points="592,404 610,404 598,414 598,479 592,479" fill="var(--steel-deep)"/>
    <circle class="lamp-rim" cx="550" cy="439" r="20" fill="url(#lamp-bezel)"/>
    <circle class="lamp-seat" cx="550" cy="439" r="17" fill="var(--lock-shadow)"/>
    <circle class="lamp" cx="550" cy="439" r="14" fill="url(#lamp-glow)"/>
    <circle class="lamp-rim" cx="650" cy="439" r="20" fill="url(#lamp-bezel)"/>
    <circle class="lamp-seat" cx="650" cy="439" r="17" fill="var(--lock-shadow)"/>
    <circle class="lamp" cx="650" cy="439" r="14" fill="url(#lamp-glow)"/>
  </g>
</svg>
</body>
</html>
```